Business Card Design Project

We need a business card design for a new construction company called 'KORVA HOLDINGS PTY.LTD' We run a construction based company for high end market homes in melbourne, we want something that looks professional and eye catching.The card needs to have a strong design to it something modern as the company name explains "korva." The final design should communicate professionalism and a strong image to our customers on the quality of our work.
On the business card i need
Name: Marek Holtvay
Mob:0417295031
Email:korva.holdings@mailbrook.example
Domestic/Residential/Commercial

```html
<!DOCTYPE html>
<html lang="en">
<head>
<meta charset="utf-8">
<title>Korva Holdings – Business Cards</title>
<link rel="stylesheet" href="https://fonts.googleapis.com/css2?family=Fira+Sans:wght@400;500;600&display=swap">
<style>
  :root {
    --stage: #d6d6d8;
    --ink: #231f20;
    --paper: #ffffff;
    --accent: #e0262b;
    --muted: #a9a8a8;
    --shadow: 0 6px 18px rgba(0,0,0,0.55);
  }
  * { box-sizing: border-box; margin: 0; padding: 0; }
  html, body {
    width: 1200px; height: 730px; overflow: hidden;
    background: var(--stage);
    font-family: "Fira Sans", Arial, sans-serif;
  }
  .canvas { position: relative; width: 1200px; height: 730px; }
  .card {
    position: absolute; width: 500px; height: 277px;
    box-shadow: var(--shadow); overflow: hidden;
  }
  .card--front { left: 73px; top: 77px; background: var(--paper); }
  .card--back { left: 73px; top: 390px; background: var(--ink); }
  .card--combined { left: 650px; top: 253px; background: var(--ink); }

  .brand { position: absolute; left: 0; right: 0; text-align: center; }
  .brand__name {
    display: inline-flex; align-items: center; gap: 8px;
    font-size: 58px; font-weight: 600; color: var(--ink);
    letter-spacing: 1px; line-height: 1;
  }
  .brand__dot { width: 10px; height: 10px; border-radius: 50%; background: var(--accent); }
  .brand__legal {
    margin-top: 6px; font-size: 9px; font-weight: 500;
    letter-spacing: 4.5px; color: var(--accent);
  }
  .card--front .brand { top: 105px; }

  .contact { position: absolute; left: 0; right: 0; text-align: center; color: var(--paper); }
  .contact__name { font-size: 17px; color: var(--accent); margin-bottom: 17px; }
  .contact__line { font-size: 13.5px; line-height: 18px; }
  .card--back .contact { top: 92px; }

  .services { position: absolute; left: 0; right: 0; text-align: center; font-size: 16px; }
  .services__sep { color: var(--accent); }
  .card--back .services { top: 238px; color: var(--muted); }
  .card--combined .services { top: 23px; color: var(--accent); }
  .card--combined .services__sep { color: var(--accent); }

  .band { position: absolute; left: 0; top: 62px; width: 500px; height: 117px; background: var(--paper); }
  .card--combined .brand { top: 92px; }
  .card--combined .contact { top: 192px; }
  .card--combined .contact__name { font-size: 16px; margin-bottom: 13px; }
  .card--combined .contact__line { font-size: 13.5px; line-height: 16px; }
</style>
</head>
<body>
<main class="canvas">

  <section class="card card--front" aria-label="Card front">
    <div class="brand">
      <div class="brand__name">korva<span class="brand__dot"></span></div>
      <div class="brand__legal">KORVA HOLDINGS PTY.LTD</div>
    </div>
  </section>

  <section class="card card--back" aria-label="Card back">
    <div class="contact">
      <p class="contact__name">Marek Holtvay</p>
      <p class="contact__line">Mobile: 0417 295031</p>
      <p class="contact__line">korva.holdings@mailbrook.example</p>
    </div>
    <p class="services">Domestic <span class="services__sep">•</span> Residential <span class="services__sep">•</span> Commercial</p>
  </section>

  <section class="card card--combined" aria-label="Single-sided card">
    <p class="services">Domestic <span class="services__sep">•</span> Residential <span class="services__sep">•</span> Commercial</p>
    <div class="band"></div>
    <div class="brand">
      <div class="brand__name">korva<span class="brand__dot"></span></div>
      <div class="brand__legal">KORVA HOLDINGS PTY.LTD</div>
    </div>
    <div class="contact">
      <p class="contact__name">Marek Holtvay</p>
      <p class="contact__line">Mobile: 0417 295031</p>
      <p class="contact__line">korva.holdings@mailbrook.example</p>
    </div>
  </section>

</main>
</body>
</html>
```